Email signature required - I have a logo and similar design examples

I would like an email signature similar to the examples i have uploaded. My company is Pennlatch and we are a sign company installing signs for real estate agents. i already have my logo design, i just need an email signature. I would like images similar to the samples i have attached. We are a company installing for sale signs at houses that are for sale. please see my website for further information.

These are my details i want on the signature:

Kind regards
Colin
Tel: 0333 4819573 Web: www.pennlatch.co.uk Email: colin@pennlatch.co.uk
Unit 14, Holloway Lane Industrial Estate
Fernlowe
Dunmarsh
CW12 4TD

Industry/Entity Type

Real Estate

Requirements
Must have
• graphic images like samples

```html
<!DOCTYPE html>
<html lang="en">
<head>
<meta charset="utf-8">
<title>Pennlatch email signatures</title>
<link rel="stylesheet" href="https://fonts.googleapis.com/css2?family=Nunito:wght@800&family=Roboto:wght@400&display=swap">
<style>
  :root {
    --stage: #333333;
    --band-top: #8b1c3b;
    --band-mid: #5a1d4b;
    --band-bottom: #271c58;
    --ink: #ffffff;
    --accent: #d8283a;
    --chip: #e9e6ef;
  }
  * { margin: 0; padding: 0; box-sizing: border-box; }
  html, body { width: 1200px; height: 678px; overflow: hidden; background: var(--stage); }
  body { position: relative; font-family: "Roboto", Arial, sans-serif; color: var(--ink); }

  .signature {
    position: absolute; left: 246px; width: 706px; overflow: hidden;
    background: linear-gradient(180deg, var(--band-top) 0%, var(--band-mid) 50%, var(--band-bottom) 100%);
  }
  .signature--wide { top: 113px; height: 194px; }
  .signature--tall { top: 344px; height: 221px; }

  .house-photo { position: absolute; top: 0; height: 100%; width: 222px; }
  .signature--wide .house-photo {
    left: 0;
    background: linear-gradient(160deg, #b5624a 0%, #c98a66 40%, #6e7a4a 75%, #3d4a2c 100%);
  }
  .signature--tall .house-photo {
    right: 0;
    background: linear-gradient(200deg, #8a4a3c 0%, #d09a76 40%, #b98d6a 65%, #3f4f2e 100%);
  }

  .brand-name {
    position: absolute; font-family: "Nunito", Arial, sans-serif; font-weight: 800;
    color: var(--ink); letter-spacing: -0.5px; line-height: 1; white-space: nowrap;
  }
  .signature--wide .brand-name { left: 230px; top: 34px; font-size: 52px; }
  .signature--tall .brand-name { left: 240px; top: 28px; font-size: 50px; }

  .person-name {
    position: absolute; font-family: "Nunito", Arial, sans-serif; font-weight: 800;
    font-size: 25px; line-height: 1; white-space: nowrap;
  }
  .person-role { position: absolute; font-size: 13px; line-height: 1; white-space: nowrap; }
  .signature--wide .person-name { left: 245px; top: 121px; }
  .signature--wide .person-role { left: 245px; top: 149px; }
  .signature--tall .person-name { left: 26px; top: 17px; }
  .signature--tall .person-role { left: 26px; top: 45px; }

  .social { position: absolute; display: flex; gap: 6px; }
  .social span { width: 23px; height: 23px; border-radius: 50%; background: var(--chip); display: block; }
  .signature--wide .social { left: 588px; top: 24px; }
  .signature--tall .social { left: 348px; top: 178px; }

  .contact-list { position: absolute; list-style: none; font-size: 14.5px; line-height: 21.5px; }
  .contact-list li { display: flex; align-items: center; gap: 8px; white-space: nowrap; }
  .contact-list svg { width: 13px; height: 13px; fill: var(--accent); flex: none; }
  .signature--wide .contact-list { right: 24px; top: 65px; text-align: right; }
  .signature--wide .contact-list li { justify-content: flex-end; }
  .signature--tall .contact-list { left: 27px; top: 139px; }
  .signature--tall .contact-list li { gap: 10px; }

  .address { position: absolute; font-size: 14.5px; line-height: 21px; font-style: normal; white-space: nowrap; }
  .signature--wide .address { right: 24px; top: 134px; text-align: right; }
  .signature--tall .address { left: 26px; top: 89px; }
</style>
</head>
<body>

<svg width="0" height="0" style="position:absolute" aria-hidden="true">
  <symbol id="icon-phone" viewBox="0 0 16 16"><path d="M1 5c0-2 3-3 7-3s7 1 7 3v1h-4V5H5v1H1z M4 7h8l2 6H2z"/></symbol>
  <symbol id="icon-mail" viewBox="0 0 16 16"><path d="M1 3l7 6 7-6v10H1z"/></symbol>
  <symbol id="icon-globe" viewBox="0 0 16 16"><path d="M8 1a7 7 0 1 0 0 14A7 7 0 0 0 8 1zm0 1.5c.8 0 1.6 1.8 1.9 4.5H6.1C6.4 4.3 7.2 2.5 8 2.5zM2.6 7h2.1c.1-1.7.4-3.1.9-4A5.6 5.6 0 0 0 2.6 7zm8.7 0h2.1a5.6 5.6 0 0 0-3-4c.5.9.8 2.3.9 4zM2.6 9a5.6 5.6 0 0 0 3 4c-.5-.9-.8-2.3-.9-4zm3.5 0c.3 2.7 1.1 4.5 1.9 4.5s1.6-1.8 1.9-4.5zm5.2 0c-.1 1.7-.4 3.1-.9 4a5.6 5.6 0 0 0 3-4z"/></symbol>
</svg>

<section class="signature signature--wide">
  <div class="house-photo" role="img" aria-label="Photo of a brick house with a for sale board in the front garden"></div>
  <div class="brand-name">Pennlatch</div>
  <div class="person-name">Colin Hartley</div>
  <div class="person-role">Sales Director</div>
  <div class="social" aria-label="Social links"><span></span><span></span><span></span></div>
  <ul class="contact-list">
    <li>0333 4819573 <svg><use href="#icon-phone"/></svg></li>
    <li>www.pennlatch.co.uk <svg><use href="#icon-mail"/></svg></li>
    <li>colin@pennlatch.co.uk <svg><use href="#icon-globe"/></svg></li>
  </ul>
  <address class="address">Unit 14, Holloway Lane Industrial Estate<br>Fernlowe Dunmarsh CW12 4TD</address>
</section>

<section class="signature signature--tall">
  <div class="house-photo" role="img" aria-label="Photo of a brick house gable with a for sale board beside it"></div>
  <div class="person-name">Colin Hartley</div>
  <div class="person-role">Sales Director</div>
  <div class="brand-name">Pennlatch</div>
  <address class="address">Unit 14, Holloway Lane Industrial Estate<br>Fernlowe Dunmarsh CW12 4TD</address>
  <ul class="contact-list">
    <li><svg><use href="#icon-phone"/></svg> 0333 4819573</li>
    <li><svg><use href="#icon-mail"/></svg> www.pennlatch.co.uk</li>
    <li><svg><use href="#icon-globe"/></svg> colin@pennlatch.co.uk</li>
  </ul>
  <div class="social" aria-label="Social links"><span></span><span></span><span></span></div>
</section>

</body>
</html>
```